Business Card Design

We do Metal Roofing, fascia and gutter and edge protection [safety rail].

Industry/Entity Type

Business

Contact Information for Business Card

Tarnwell Roof Plumbing. Metal Roofing, Fascia and Gutter, Edge Protection
Colin 0468305172
Finn 0419587364
tr7win5@mailvane.com
Lic: 614903K
ABN:52716340951

```html
<!DOCTYPE html>
<html lang="en">
<head>
<meta charset="utf-8">
<title>Tarnwell Roof Plumbing – Business Card</title>
<link rel="stylesheet" href="https://fonts.googleapis.com/css2?family=PT+Sans:wght@400;700&display=swap">
<style>
  :root {
    --backdrop: #dadada;
    --card: #ffffff;
    --brand-red: #e3171f;
    --ink-dark: #333333;
    --ink-body: #2a2a2a;
  }
  * { margin: 0; padding: 0; box-sizing: border-box; }
  html, body {
    width: 1200px;
    height: 900px;
    overflow: hidden;
  }
  body {
    background: var(--backdrop);
    font-family: "PT Sans", Arial, sans-serif;
    position: relative;
  }
  .card {
    position: absolute;
    top: 306px;
    width: 440px;
    height: 271px;
    background: var(--card);
    border-radius: 12px;
  }
  .card--front { left: 149px; }
  .card--back  { left: 608px; }

  /* Front: brand lockup */
  .brand-lockup {
    position: absolute;
    left: 46px;
    top: 76px;
  }
  .brand-name {
    color: var(--brand-red);
    font-size: 50px;
    font-weight: 400;
    line-height: 1;
    letter-spacing: 0.5px;
  }
  .brand-trade {
    margin-top: 14px;
    color: var(--ink-dark);
    font-size: 24px;
    font-weight: 700;
    line-height: 1;
  }

  /* Front: contact block */
  .contact {
    position: absolute;
    left: 251px;
    top: 68px;
    color: var(--ink-body);
    font-size: 12.5px;
    line-height: 15px;
  }
  .contact-person + .contact-person { margin-top: 10px; }
  .contact-name {
    color: var(--brand-red);
    font-size: 15px;
    font-weight: 700;
    line-height: 17px;
  }
  .contact-email {
    display: flex;
    align-items: center;
    gap: 5px;
    margin-top: 9px;
  }
  .contact-email svg { width: 9px; height: 7px; }
  .contact-legal { margin-top: 9px; line-height: 16px; }

  /* Back */
  .back-name {
    position: absolute;
    left: 0;
    right: 0;
    top: 88px;
    text-align: center;
    color: var(--brand-red);
    font-size: 68px;
    font-weight: 400;
    line-height: 1;
    letter-spacing: 1px;
  }
  .back-services {
    position: absolute;
    left: 0;
    right: 0;
    top: 222px;
    text-align: center;
    color: var(--brand-red);
    font-size: 12.5px;
    font-weight: 700;
  }
</style>
</head>
<body>
  <section class="card card--front" aria-label="Card front">
    <div class="brand-lockup">
      <div class="brand-name">Tarnwell</div>
      <div class="brand-trade">Roof Plumbing</div>
    </div>
    <div class="contact">
      <div class="contact-person">
        <div class="contact-name">Colin</div>
        <div class="contact-phone">0468305172</div>
      </div>
      <div class="contact-person">
        <div class="contact-name">Finn</div>
        <div class="contact-phone">0419587364</div>
      </div>
      <div class="contact-email">
        <svg viewBox="0 0 9 7" aria-hidden="true">
          <rect x="0" y="0" width="9" height="7" rx="1" fill="var(--brand-red)"/>
          <path d="M0.8 1 L4.5 4 L8.2 1" fill="none" stroke="#fff" stroke-width="0.9"/>
        </svg>
        <span>tr7win5@mailvane.com</span>
      </div>
      <div class="contact-legal">
        <div>Lic: 614903K</div>
        <div>ABN:52716340951</div>
      </div>
    </div>
  </section>

  <section class="card card--back" aria-label="Card back">
    <div class="back-name">Tarnwell</div>
    <div class="back-services">Metal Roofing, Fascia and Gutter, Edge Protection</div>
  </section>
</body>
</html>
```